Business card design incorporating discount offer

We are a trade services company and we need a double sided business card that is going to be used by our tradesmen to give to customers on completion of their jobs.

Below are the key elements of the card that we would like to include:

-Main logo with text 'Corvane Building Aid' underneath.
-Up to 12 smaller icon logos with text 'Your local all-trade experts' to emphasise the point that we cover all the trades
-Discount offer - 10% discount
-Telephone number and website address
-Blank space for tradesman to enter his/her name
-Request for customer feedback with feedback url

This business card will be printed on regular card. In the past we have favoured designs that use a black background but we're open to new ideas.

I have attached a few files:

-A simple wire frame example to show how this card could look with the different elements mentioned above, feel free to use a layout similar to this or come up with something totally different (biz-card.pdf)
-Front and back of a loyalty card the we've used in the past (this card was printed on plastic)
-Front and back of a key fob design that we've previously used (this card was printed on plastic)
-A logo file with the 12 small icons and the main logo image

If you need further images or information please ask.

```html
<!DOCTYPE html>
<html lang="en">
<head>
<meta charset="utf-8">
<title>Corvane Building Aid – Business Card</title>
<link href="https://fonts.googleapis.com/css2?family=Comfortaa:wght@300;400;700&display=swap" rel="stylesheet">
<style>
  :root {
    --backdrop: #ece9e4;
    --card: #ffffff;
    --ink-grey: #9a9a9a;
    --ink-soft: #b3b3b3;
    --brand-blue: #1aa6d6;
    --brand-blue-deep: #0e86c4;
    --brand-cyan: #2fc0e6;
    --rule: #7cc7e4;
    --tile-sky: #3aa7e0;
    --tile-red: #d8262f;
    --tile-green: #6dbb3a;
    --tile-yellow: #f0c419;
    --tile-teal: #2bb6a3;
    --tile-grey: #8a8f96;
    --tile-blue: #2e8fd8;
    --tile-orange: #e8a93a;
    --tile-slate: #6f8fa8;
    --tile-purple: #a0318e;
    --tile-tan: #b68b5e;
  }
  * { box-sizing: border-box; margin: 0; padding: 0; }
  html, body { width: 1200px; height: 901px; overflow: hidden; }
  body {
    background: var(--backdrop);
    font-family: "Comfortaa", sans-serif;
    position: relative;
  }
  .card {
    position: absolute;
    width: 560px;
    height: 362px;
    background: var(--card);
    box-shadow: 0 8px 24px rgba(0,0,0,.18);
    overflow: hidden;
  }
  /* ---------- Front ---------- */
  .card--front { left: 20px; top: 270px; }
  .brand {
    position: absolute; left: 40px; top: 48px;
    display: flex; align-items: center; gap: 14px;
  }
  .brand__mark { width: 34px; height: 34px; background: var(--ink-soft); }
  .brand__name { font-weight: 700; font-size: 54px; color: var(--ink-soft); letter-spacing: 1px; }
  .tagline {
    position: absolute; left: 40px; top: 132px;
    font-weight: 700; font-size: 27px; color: var(--ink-soft);
  }
  .contact { position: absolute; left: 40px; bottom: 44px; list-style: none; }
  .contact li {
    display: flex; align-items: center; gap: 10px;
    font-size: 14px; color: var(--ink-grey); margin-top: 8px; letter-spacing: .5px;
  }
  .contact svg { width: 16px; height: 16px; }
  .offer {
    position: absolute; right: 0; top: 0; width: 160px; height: 100%;
    background: linear-gradient(160deg, var(--brand-cyan), var(--brand-blue-deep));
    color: #fff; display: flex; flex-direction: column; justify-content: center;
    padding-left: 16px;
  }
  .offer__value { font-weight: 300; font-size: 64px; line-height: 1; }
  .offer__label { font-weight: 400; font-size: 30px; line-height: 1.1; }
  .offer__note { font-weight: 400; font-size: 15px; letter-spacing: 1px; }
  /* ---------- Back ---------- */
  .card--back { left: 620px; top: 270px; }
  .trades {
    position: absolute; left: 0; top: 0; width: 150px; height: 100%;
    background: linear-gradient(180deg, var(--brand-blue), var(--brand-blue-deep));
    display: grid; grid-template-columns: 48px 48px; grid-auto-rows: 48px;
    gap: 8px 12px; padding: 17px 0 0 22px;
  }
  .trade { border-radius: 9px; box-shadow: inset 0 -4px 0 rgba(0,0,0,.15); }
  .trade--sky { background: var(--tile-sky); }
  .trade--red { background: var(--tile-red); }
  .trade--green { background: var(--tile-green); }
  .trade--yellow { background: var(--tile-yellow); }
  .trade--teal { background: var(--tile-teal); }
  .trade--grey { background: var(--tile-grey); }
  .trade--blue { background: var(--tile-blue); }
  .trade--orange { background: var(--tile-orange); }
  .trade--slate { background: var(--tile-slate); }
  .trade--purple { background: var(--tile-purple); }
  .trade--tan { background: var(--tile-tan); }
  .details { position: absolute; left: 150px; right: 0; top: 0; bottom: 0; padding: 34px 26px 0 30px; }
  .details__title { font-weight: 700; font-size: 24px; color: var(--brand-blue); }
  .tradesman { margin-top: 42px; font-size: 14px; color: var(--brand-blue); }
  .write-line { border-bottom: 1px dotted var(--ink-soft); height: 26px; margin-left: 40px; }
  .divider { border: 0; border-top: 1px solid var(--rule); margin-top: 22px; }
  .feedback__question { margin-top: 18px; font-size: 16px; color: var(--brand-blue); }
  .feedback__button {
    margin: 12px 0 0 30px; background: var(--brand-cyan); color: #fff;
    border-radius: 24px; padding: 10px 0; text-align: center;
    font-size: 13px; letter-spacing: 1.5px; line-height: 1.45;
  }
</style>
</head>
<body>
  <section class="card card--front" aria-label="Card front">
    <div class="brand">
      <span class="brand__mark"></span>
      <span class="brand__name">Corvane</span>
    </div>
    <p class="tagline">Corvane Building Aid</p>
    <ul class="contact">
      <li>
        <svg viewBox="0 0 16 16" aria-hidden="true"><circle cx="8" cy="8" r="7" fill="none" stroke="#9a9a9a" stroke-width="1.4"/><path d="M5.5 4.5c0 3.5 2.5 6.5 5.5 7l.8-1.6-1.8-1-.9.9c-1-.5-1.8-1.4-2.2-2.4l.9-.8-.9-1.9z" fill="#9a9a9a"/></svg>
        0800 123 4567
      </li>
      <li>
        <svg viewBox="0 0 16 16" aria-hidden="true"><g fill="none" stroke="#9a9a9a" stroke-width="1.2"><circle cx="8" cy="8" r="7"/><ellipse cx="8" cy="8" rx="3" ry="7"/><path d="M1 8h14M2.5 4.5h11M2.5 11.5h11"/></g></svg>
        www.corvane-aid.co.uk
      </li>
    </ul>
    <div class="offer">
      <span class="offer__value">10%</span>
      <span class="offer__label">Discount</span>
      <span class="offer__note">with this card</span>
    </div>
  </section>

  <section class="card card--back" aria-label="Card back">
    <div class="trades">
      <div class="trade trade--sky" role="img" aria-label="Building trade icon"></div>
      <div class="trade trade--blue" role="img" aria-label="Water trade icon"></div>
      <div class="trade trade--red" role="img" aria-label="Decorating trade icon"></div>
      <div class="trade trade--green" role="img" aria-label="Pest control trade icon"></div>
      <div class="trade trade--yellow" role="img" aria-label="Cleaning trade icon"></div>
      <div class="trade trade--teal" role="img" aria-label="Appliance trade icon"></div>
      <div class="trade trade--grey" role="img" aria-label="Electrical trade icon"></div>
      <div class="trade trade--blue" role="img" aria-label="Gas trade icon"></div>
      <div class="trade trade--orange" role="img" aria-label="Carpentry trade icon"></div>
      <div class="trade trade--slate" role="img" aria-label="Plumbing trade icon"></div>
      <div class="trade trade--purple" role="img" aria-label="Bathroom trade icon"></div>
      <div class="trade trade--tan" role="img" aria-label="Handyman trade icon"></div>
    </div>
    <div class="details">
      <h2 class="details__title">Your local all-trade experts</h2>
      <p class="tradesman">Your Corvane tradesman:</p>
      <div class="write-line"></div>
      <div class="write-line"></div>
      <hr class="divider">
      <p class="feedback__question">What do you think about our service?</p>
      <div class="feedback__button">Leave your feedback online<br>www.corvane-aid.co.uk/feedback</div>
    </div>
  </section>
</body>
</html>
```